NEW YORK Plumbing/utility company 10 year anniversary business card

Looking For simple back and front business card would like to include a few things in description
We offer 24/7 emergency service
residential
commercial
industrial
municipal
services offered
Plumbing
hydro excavation
hydro jetting
Well pumps
Sewer pumps
water mains
sewer mains

```html
<!DOCTYPE html>
<html lang="en">
<head>
<meta charset="utf-8">
<title>Ridgeline Water &amp; Sewer – Business Card</title>
<link href="https://fonts.googleapis.com/css2?family=Cabin:wght@500;600;700&display=swap" rel="stylesheet">
<style>
  :root {
    --backdrop: #ababab;
    --navy: #01619e;
    --cyan: #06cbf9;
    --white: #ffffff;
  }
  html, body {
    margin: 0;
    padding: 0;
    width: 1200px;
    height: 1200px;
    overflow: hidden;
    background: var(--backdrop);
    font-family: "Cabin", Arial, sans-serif;
  }
  .card {
    position: absolute;
    left: 181px;
    width: 850px;
    height: 459px;
    background: var(--white);
    overflow: hidden;
  }
  .card--front { top: 91px; }
  .card--back { top: 649px; }

  .wave-area {
    position: absolute;
  }
  .card--front .wave-area {
    left: 0;
    right: 0;
    bottom: 0;
    height: 170px;
    background: linear-gradient(180deg, var(--cyan) 0%, var(--navy) 55%, var(--navy) 100%);
  }
  .card--back .wave-area {
    left: 0;
    top: 0;
    bottom: 0;
    width: 560px;
    background: linear-gradient(90deg, var(--navy) 0%, var(--navy) 80%, #0a8fd0 100%);
  }

  .brand {
    position: absolute;
    display: flex;
    align-items: center;
    justify-content: center;
    gap: 12px;
    color: var(--navy);
    font-weight: 700;
    text-transform: uppercase;
  }
  .brand__dot {
    width: 22px;
    height: 22px;
    border-radius: 50%;
    background: var(--cyan);
    flex: none;
  }
  .brand__name {
    line-height: 1.05;
    text-align: center;
  }
  .brand__name span { display: block; }
  .brand__first { font-size: 50px; letter-spacing: 4px; }
  .brand__second { font-size: 21px; letter-spacing: 4px; margin-top: 6px; }
  .card--front .brand { left: 265px; top: 150px; width: 320px; }
  .card--back .brand { left: 570px; top: 75px; width: 270px; }
  .card--back .brand__first { font-size: 44px; letter-spacing: 3px; }
  .card--back .brand__second { font-size: 19px; letter-spacing: 3px; }

  .contact {
    position: absolute;
    left: 25px;
    top: 142px;
    margin: 0;
    padding: 0;
    list-style: none;
    color: var(--white);
    font-size: 18px;
    font-weight: 600;
  }
  .contact li {
    display: flex;
    align-items: center;
    height: 31px;
  }
  .contact svg {
    width: 16px;
    height: 16px;
    margin-right: 21px;
    fill: var(--white);
    flex: none;
  }
  .info-block {
    position: absolute;
    top: 276px;
    color: var(--white);
  }
  .info-block__title {
    margin: 0;
    font-size: 18px;
    font-weight: 700;
    padding-bottom: 9px;
    border-bottom: 1.5px solid var(--cyan);
  }
  .info-block__cols {
    display: flex;
    gap: 40px;
    margin-top: 9px;
  }
  .info-block ul {
    margin: 0;
    padding: 0;
    list-style: none;
    font-size: 18px;
    font-weight: 600;
    line-height: 24px;
    white-space: nowrap;
  }
  .info-block--services { left: 25px; width: 290px; }
  .info-block--capacity { left: 358px; width: 99px; }
</style>
</head>
<body>

<section class="card card--front" aria-label="Business card front">
  <div class="wave-area" role="img" aria-label="Decorative water wave band"></div>
  <div class="brand">
    <span class="brand__dot"></span>
    <div class="brand__name"><span class="brand__first">Ridgeline</span><span class="brand__second">Water &amp; Sewer</span></div>
  </div>
</section>

<section class="card card--back" aria-label="Business card back">
  <div class="wave-area" role="img" aria-label="Decorative water wave panel"></div>

  <div class="brand">
    <span class="brand__dot"></span>
    <div class="brand__name"><span class="brand__first">Ridgeline</span><span class="brand__second">Water &amp; Sewer</span></div>
  </div>

  <ul class="contact">
    <li><svg viewBox="0 0 16 16"><path d="M8 0a5.5 5.5 0 0 0-5.5 5.5C2.5 9.6 8 16 8 16s5.5-6.4 5.5-10.5A5.5 5.5 0 0 0 8 0zm0 8a2.5 2.5 0 1 1 0-5 2.5 2.5 0 0 1 0 5z"/></svg>Address</li>
    <li><svg viewBox="0 0 16 16"><path d="M3.6 1.2l2.3 2.6-1.2 2a9 9 0 0 0 5.5 5.5l2-1.2 2.6 2.3-1.4 2.3C7.2 14.5 1.5 8.8 1.3 2.6z"/></svg>+00 1234 5678 9012</li>
    <li><svg viewBox="0 0 16 16"><path d="M0 3h16v1.2L8 9 0 4.2zm0 2.6l5.2 3.1L0 13zm16 0V13l-5.2-4.3zM6.3 9.4L8 10.5l1.7-1.1L15.5 13H.5z"/></svg>hello@ridgelinews.com</li>
    <li><svg viewBox="0 0 16 16"><path d="M3 0l10 9.5-4.3.3 2.6 5.3-1.8.9-2.6-5.4L3 14z"/></svg>&nbsp;www.ridgelinews.com</li>
  </ul>

  <div class="info-block info-block--services">
    <h2 class="info-block__title">Services Offered:</h2>
    <div class="info-block__cols">
      <ul>
        <li>Plumbing</li>
        <li>Hydro excavation</li>
        <li>Hydro jetting</li>
        <li>Well pumps</li>
      </ul>
      <ul>
        <li>Sewer pumps</li>
        <li>Water mains</li>
        <li>Sewer mains</li>
      </ul>
    </div>
  </div>

  <div class="info-block info-block--capacity">
    <h2 class="info-block__title">Capacity:</h2>
    <div class="info-block__cols">
      <ul>
        <li>Residential</li>
        <li>Commercial</li>
        <li>Industrial</li>
        <li>Municipal</li>
      </ul>
    </div>
  </div>
</section>

</body>
</html>
```